Brisa Pastry Mill Business card

We are empanada whole-sellers and I want a business card design with a picture of an empanada on it that also mentions first trial order FREE. our contact number 555-214-7093 our website www.brisapastry.example and business email Tobin@brisapastry.example

If you want any of our artwork please feel free to email me at the address above.

```html
<!DOCTYPE html>
<html lang="en">
<head>
<meta charset="utf-8">
<title>Brisa Pastry Mill – Business Card</title>
<link rel="stylesheet" href="https://fonts.googleapis.com/css2?family=Arvo:wght@400;700&family=Oswald:wght@600;700&display=swap">
<style>
  :root {
    --card-yellow: #f2b51d;
    --ring-orange: #f7931e;
    --ink: #141414;
    --paper: #ffffff;
    --pastry-light: #f4ede0;
    --pastry-shade: #d9cdb6;
  }
  * { margin: 0; padding: 0; box-sizing: border-box; }
  html, body { width: 1200px; height: 720px; overflow: hidden; background: var(--card-yellow); }
  .card {
    position: relative; width: 1200px; height: 720px; overflow: hidden;
    background: var(--card-yellow);
    font-family: "Arvo", Georgia, serif; color: var(--ink);
  }
  .blossom { position: absolute; border-radius: 50%; background: var(--ink); }
  .blossom--top-left { left: 20px; top: -40px; width: 200px; height: 200px; }
  .blossom--top-right { left: 1075px; top: -60px; width: 150px; height: 150px; }
  .blossom--small { left: 1072px; top: 352px; width: 56px; height: 56px; }
  .blossom--bottom-right { left: 1060px; top: 560px; width: 220px; height: 220px; }
  .blossom--bottom-left { left: 160px; top: 578px; width: 145px; height: 145px; }

  .offer-badge {
    position: absolute; left: -8px; top: 93px; width: 534px; height: 534px;
    border-radius: 50%; background: var(--ring-orange);
  }
  .offer-badge__frame {
    position: absolute; left: 20px; top: 20px; width: 494px; height: 494px;
    border-radius: 50%; background: var(--ink);
  }
  .offer-badge__photo {
    position: absolute; left: 16px; top: 16px; width: 462px; height: 462px;
    border-radius: 50%;
    background: radial-gradient(circle at 45% 40%, var(--pastry-light) 0%, var(--pastry-light) 45%, var(--pastry-shade) 100%);
  }
  .offer-badge__text {
    position: absolute; left: 115px; top: 312px; width: 360px;
    transform: rotate(-8deg); text-align: center;
    font-family: "Oswald", "Arial Narrow", sans-serif; font-weight: 700;
    text-transform: uppercase; line-height: 1.02; color: var(--ink);
    text-shadow: 0 0 3px var(--paper), 0 0 3px var(--paper), 0 0 4px var(--paper);
  }
  .offer-badge__line { display: block; font-size: 40px; }
  .offer-badge__line--lead { font-size: 54px; }
  .offer-badge__line--free { font-size: 78px; }

  .brand-name {
    position: absolute; left: 420px; top: 110px; width: 640px; text-align: center;
    font-weight: 700; font-size: 64px; line-height: 1.05; color: var(--ink);
  }
  .brand-rule {
    position: absolute; left: 556px; top: 238px; width: 270px; height: 3px;
    background: var(--ink);
  }
  .brand-rule::before, .brand-rule::after {
    content: ""; position: absolute; top: -3px; width: 9px; height: 9px;
    border-radius: 50%; background: var(--ink);
  }
  .brand-rule::before { left: -4px; }
  .brand-rule::after { right: -4px; }
  .brand-tagline {
    position: absolute; left: 560px; top: 252px; width: 270px;
    font-weight: 700; font-size: 31px; text-transform: uppercase; letter-spacing: 0.5px;
  }

  .pitch {
    position: absolute; left: 530px; top: 337px; width: 540px; text-align: center;
    font-weight: 700; text-transform: uppercase; line-height: 1.12;
  }
  .pitch__small { display: block; font-size: 28px; }
  .pitch__large { display: block; font-size: 44px; margin-top: 2px; }

  .contact {
    position: absolute; left: 530px; top: 492px; width: 540px; text-align: center;
    font-weight: 700; font-size: 28px; line-height: 1.5; text-transform: uppercase;
  }
  .contact__row { display: flex; align-items: center; justify-content: center; gap: 10px; }
  .contact__row--web { text-transform: none; font-size: 26px; line-height: 1.45; }
  .contact__icon { width: 28px; height: 28px; flex: none; }
  .contact__mark { width: 22px; height: 22px; background: var(--ink); flex: none; }
</style>
</head>
<body>
<main class="card">
  <div class="blossom blossom--top-left" role="img" aria-label="Black decorative flower"></div>
  <div class="blossom blossom--top-right" role="img" aria-label="Black decorative flower"></div>
  <div class="blossom blossom--small" role="img" aria-label="Small black decorative flower"></div>
  <div class="blossom blossom--bottom-right" role="img" aria-label="Black decorative flower"></div>

  <section class="offer-badge">
    <div class="offer-badge__frame">
      <div class="offer-badge__photo" role="img" aria-label="Photo of frozen uncooked empanadas stacked together"></div>
    </div>
  </section>
  <div class="blossom blossom--bottom-left" role="img" aria-label="Black decorative flower"></div>
  <p class="offer-badge__text">
    <span class="offer-badge__line offer-badge__line--lead">First Trial</span>
    <span class="offer-badge__line">Order of</span>
    <span class="offer-badge__line">Empanadas for</span>
    <span class="offer-badge__line offer-badge__line--free">Free</span>
  </p>

  <h1 class="brand-name">Brisa Pastry Mill</h1>
  <div class="brand-rule" aria-hidden="true"></div>
  <p class="brand-tagline">Empanadas</p>

  <p class="pitch">
    <span class="pitch__small">We sell</span>
    <span class="pitch__small">Frozen empanadas at</span>
    <span class="pitch__large">Wholesaler price</span>
  </p>

  <div class="contact">
    <div class="contact__row">
      <svg class="contact__icon" viewBox="0 0 28 28" aria-hidden="true">
        <circle cx="14" cy="14" r="13" fill="#141414"/>
        <path d="M10 7.5c-.8 0-1.8 1-1.8 2.3 0 4.6 5.4 10 10 10 1.3 0 2.3-1 2.3-1.8l-.2-.7-2.6-1.2-1.4 1.3c-1.7-.7-3.3-2.3-4-4l1.3-1.4-1.2-2.6z" fill="#f2b51d"/>
      </svg>
      <span>555-214-7093</span>
    </div>
    <div class="contact__row">
      <span class="contact__mark" aria-hidden="true"></span>
      <span>@BRISAPASTRY</span>
    </div>
    <div class="contact__row contact__row--web">
      <span>www.brisapastry.example</span>
    </div>
    <div class="contact__row contact__row--web">
      <span>Tobin@brisapastry.example</span>
    </div>
  </div>
</main>
</body>
</html>
```